Medien Firma benötigt Briefpapier
Zielgruppe
Firma:
Wir sind im Bereich Veranstaltungstechnik und Eventmanagement seit 2007 tätig. Ab 2009 konnten wir unsere Expertise um die Bereiche Medientechnik und TV Produktion erweitern. Durch dieses Portfolio sind wir in der Lage, alle Facetten der technischen Planung durchzuführen.
Bereiche:
Veranstaltungstechnik - Medientechnik - Livestreaming
Kunden:
B2B
Aufgabenstellung
Erstellung von Briefpapier mit dem vorhandenen Logo.
Das Briefpapier soll auch als Produktsheet nutzbar sein. Also muss der Footer Text austauschbar sein.
Schlicht, Modern, Zeitlos, max. zwei Farben

```html
<!DOCTYPE html>
<html lang="de">
<head>
<meta charset="utf-8">
<title>lumenhaus – Briefpapier und Produktsheet</title>
<link rel="stylesheet" href="https://fonts.googleapis.com/css2?family=Raleway:wght@300;400;600&display=swap">
<style>
  :root {
    --backdrop: #97a7ae;
    --paper: #ffffff;
    --brand-blue: #009bdf;
    --ink: #1a1a1a;
    --ink-soft: #3a3a3a;
    --rule: #9fd3ee;
  }
  * { margin: 0; padding: 0; box-sizing: border-box; }
  html, body {
    width: 1200px; height: 960px; overflow: hidden;
    background: var(--backdrop);
    font-family: "Raleway", sans-serif;
  }
  .canvas { position: relative; width: 1200px; height: 960px; }

  .sheet {
    position: absolute; top: 101px;
    width: 536px; height: 758px;
    background: var(--paper);
    overflow: hidden;
  }
  .sheet--letter { left: 24px; }
  .sheet--product { left: 632px; }

  /* Wordmark */
  .wordmark {
    position: absolute;
    display: flex; align-items: center;
    font-family: "Raleway", sans-serif;
    font-weight: 400;
    color: var(--ink);
    letter-spacing: 0.01em;
    line-height: 1;
  }
  .wordmark__dot {
    flex: none;
    border: 1.5px solid var(--brand-blue);
    border-radius: 50%;
  }
  .sheet--letter .wordmark { right: 25px; top: 95px; font-size: 22px; gap: 6px; }
  .sheet--letter .wordmark__dot { width: 17px; height: 17px; }
  .sheet--product .wordmark { right: 25px; top: 685px; font-size: 34px; gap: 9px; }
  .sheet--product .wordmark__dot { width: 28px; height: 28px; border-width: 2px; }

  /* Sender line */
  .sender { position: absolute; left: 64px; top: 114px; font-size: 5.5px; line-height: 8px; color: var(--ink-soft); }
  .sender__name { color: var(--brand-blue); font-weight: 600; }

  /* Footer */
  .footer-rule {
    position: absolute; left: 64px; top: 662px;
    width: 409px; height: 1px; background: var(--rule);
  }
  .footer-mark {
    position: absolute; left: 63px; top: 674px;
    width: 43px; height: 43px;
    border: 1.5px solid var(--brand-blue); border-radius: 50%;
  }
  .footer-col {
    position: absolute; top: 675px;
    font-size: 6px; line-height: 7.4px; color: var(--ink-soft);
  }
  .footer-col p + p { margin-top: 2.6px; }
  .footer-col--contact { left: 222px; }
  .footer-col--bank { left: 355px; }
  .footer-col .link { color: var(--brand-blue); }

  .product-art { position: absolute; left: 0; top: 0; }
</style>
</head>
<body>
<main class="canvas">

  <section class="sheet sheet--letter" aria-label="Briefbogen">
    <div class="wordmark"><span class="wordmark__dot"></span>lumenhaus</div>

    <div class="sender">
      <p class="sender__name">lumenhaus</p>
      <p>Musterstraße 1 | 12345 Musterstadt | info@lumenhaus.de</p>
    </div>

    <div class="footer-rule"></div>
    <div class="footer-mark"></div>

    <div class="footer-col footer-col--contact">
      <p>Musterstraße 1<br>12345 Musterstadt</p>
      <p>Tel: 0123 456 789</p>
      <p>info@lumenhaus.de<br><span class="link">www.lumenhaus.de</span></p>
    </div>

    <div class="footer-col footer-col--bank">
      <p>Finanzamt Musterstadt</p>
      <p>Ust.ID: DE 123 456 789</p>
      <p>BV: Musterbank<br>BIC: ABCDEFGHI<br>IBAN: DE 1234 5678 9012 3456 7890</p>
    </div>
  </section>

  <section class="sheet sheet--product" aria-label="Produktsheet">
    <svg class="product-art" width="536" height="758" viewBox="0 0 536 758" aria-hidden="true">
      <circle cx="272" cy="278" r="237" fill="none" stroke="var(--brand-blue)" stroke-width="2"/>
      <circle cx="121" cy="525" r="121" fill="var(--brand-blue)"/>
    </svg>
    <div class="wordmark"><span class="wordmark__dot"></span>lumenhaus</div>
  </section>

</main>
</body>
</html>
```